Letterhead for Business Law Firm

We need a letter head for our firm based on the design we have settled on and it is attached. Our clients are small and large businesses around the world, and our letterhead is used typically for formal legal purposes such as demand letters (accusing the recipient of doing bad things) or responding to demand letters. It may also be sent to regulators and other government agencies. So this needs to be tasteful, but a little edgy as well - we try to convey that we are a firm that is different - businesses and investors come to us for creative, quick advice, typically in high stress circumstances, and for our ability to work through high conflict situations, and rapid paced engagements.

Target Market(s)

Lawyers, business executives, investors, government regulators who may receive letters from this firm on behalf of its clients.

Industry/Entity Type

Business

Requirements
Must have
• The design and the firm's contact information:
• Quillfen Law Firm, P.C.
• 8716 SW 19th Ave
• Portland, OR 97058
• phone: 971 555 0143
• fax: 971 555 0178
• in what placement and how depicted (e.g. a phone icon instead of the word "phone") I leave to your creative ideas.
Nice to have
• design and information can be placed at the top, bottom and/or sides of the letter, and the design should be for a standard letter size paper - and can have a separate design for the second page.

```html
<!DOCTYPE html>
<html lang="en">
<head>
<meta charset="utf-8">
<title>Quillfen Law Firm, P.C. — Letterhead</title>
<link rel="stylesheet" href="https://fonts.googleapis.com/css2?family=Montserrat:wght@200;400&display=swap">
<style>
  :root {
    --paper: #f2f2f2;
    --ink: #1f2225;
    --ink-soft: #3a3f43;
    --band-light: #9bb8c1;
    --band-mid: #6f878e;
    --band-dark: #2c3033;
    --storm-deep: #1c2326;
    --storm-teal: #3f7077;
  }
  * { margin: 0; padding: 0; box-sizing: border-box; }
  html, body { width: 867px; height: 1200px; overflow: hidden; background: var(--paper); }
  .letterhead { position: relative; width: 867px; height: 1200px; background: var(--paper); }

  .side-band {
    position: absolute; left: 0; top: 0; width: 73px; height: 1200px;
    background: linear-gradient(to right,
      var(--band-light) 0px,
      var(--band-mid) 20px,
      var(--band-dark) 33px,
      var(--band-dark) 43px,
      var(--band-mid) 56px,
      var(--band-light) 73px);
  }

  .masthead {
    position: absolute; left: 113px; top: 43px; width: 708px; height: 114px;
    display: flex; align-items: center; gap: 34px;
  }
  .masthead-mark {
    width: 114px; height: 114px; flex: none;
    background: linear-gradient(160deg, var(--storm-deep) 0%, var(--storm-teal) 100%);
    box-shadow: 4px 4px 5px rgba(0,0,0,.35);
  }
  .firm-name {
    font-family: 'Montserrat', sans-serif; font-weight: 200;
    font-size: 54px; letter-spacing: 22px; color: var(--ink);
    line-height: 1; white-space: nowrap;
  }

  .contact-bar {
    position: absolute; top: 1110px; left: 0; width: 867px; height: 30px;
  }
  .contact-item {
    position: absolute; top: 0; display: flex; align-items: center; gap: 6px;
    font-family: 'Montserrat', sans-serif; font-weight: 400;
    font-size: 9.5px; line-height: 12px; color: var(--ink-soft); white-space: nowrap;
  }
  .contact-item svg {
    width: 24px; height: 26px; flex: none;
    fill: none; stroke: var(--ink); stroke-width: 1.8; stroke-linejoin: round; stroke-linecap: round;
  }
  .item-address { left: 91px; }
  .item-phone { left: 259px; }
  .item-fax { left: 409px; }
  .item-web { left: 555px; }
  .item-mail { left: 709px; }
</style>
</head>
<body>
<div class="letterhead">
  <div class="side-band"></div>

  <header class="masthead">
    <div class="masthead-mark" role="img" aria-label="Stormy sky with lightning in dark teal tones"></div>
    <div class="firm-name">QUILLFEN</div>
  </header>

  <footer class="contact-bar">
    <div class="contact-item item-address">
      <svg viewBox="0 0 24 26" aria-hidden="true"><path d="M3 12 L12 3 L21 12 M5 10 V23 H10 V16 H14 V23 H19 V10 M16 6 V3 H18 V8"/></svg>
      <address style="font-style:normal">8716 SW 19th Ave<br>Portland, OR 97058</address>
    </div>
    <div class="contact-item item-phone">
      <svg viewBox="0 0 24 26" aria-hidden="true"><rect x="7" y="5" width="10" height="19" rx="3"/><path d="M9 1 V5"/><rect x="9" y="8" width="6" height="5"/><circle cx="12" cy="19" r="1.5"/></svg>
      <span>971 555 0143</span>
    </div>
    <div class="contact-item item-fax">
      <svg viewBox="0 0 24 26" aria-hidden="true"><path d="M7 10 V3 H17 V10"/><rect x="2" y="10" width="20" height="9" rx="2"/><rect x="7" y="16" width="10" height="7"/></svg>
      <span>971 555 0178</span>
    </div>
    <div class="contact-item item-web">
      <svg viewBox="0 0 24 26" aria-hidden="true"><circle cx="11" cy="12" r="9"/><path d="M2 12 H20 M11 3 C6 8 6 16 11 21 M11 3 C16 8 16 16 11 21"/><path d="M14 14 L14 25 L17 22 L20 26 L22 25 L19 21 L23 21 Z" fill="#1f2225"/></svg>
      <span>quillfenlaw.com</span>
    </div>
    <div class="contact-item item-mail">
      <svg viewBox="0 0 24 26" aria-hidden="true"><path d="M2 8 L21 4 L23 19 L4 23 Z M2 8 L13 15 L21 4 M4 23 L10 13 M23 19 L15 13"/></svg>
      <span>info@quillfenlaw.com</span>
    </div>
  </footer>
</div>
</body>
</html>
```